Income Tax and Accounting Brochure

I need a brochure using my new logo (file attached). I do tax work and accounting work. I am an EA (QDX Enrolled Agent - logo attached) and would like this incorporated into the brochure. I also have a MSA in Accounting. Please incorporate the text that I have provided in the brochure.

Target Market(s)

Tax Clients - both business and individuals

Industry/Entity Type

Accounting

Colors
0054AA
0677BA
7BADD7
CADEEF
E8F1F8

Requirements
Must have
• Use my logo and the QDX EA file in the brochure
Nice to have
• I would like to see a brochure that I can customize with my own text if possible.

```html
<!DOCTYPE html>
<html lang="en">
<head>
<meta charset="utf-8">
<title>Northgate Accounting &amp; Consulting – Brochure</title>
<link href="https://fonts.googleapis.com/css2?family=Montserrat:ital,wght@0,400;0,500;0,700;0,800;1,400&display=swap" rel="stylesheet">
<style>
  :root{
    --backdrop:#c4c3be;
    --ink:#1c1e24;
    --ink-soft:#2a2c33;
    --crimson:#a51b2f;
    --paper:#ececec;
    --text:#33353b;
    --brand-blue:#2a5ea8;
    --badge:#8e9a86;
  }
  *{box-sizing:border-box;margin:0;padding:0}
  html,body{width:1200px;height:889px;overflow:hidden}
  body{background:var(--backdrop);font-family:"Montserrat",sans-serif;position:relative}
  .brochure{position:absolute;left:60px;top:64px;width:1080px;height:760px;background:var(--paper);box-shadow:0 18px 40px rgba(0,0,0,.22);overflow:hidden}
  .brochure-bg{position:absolute;inset:0}
  .panel{position:absolute;top:0;width:360px;height:760px;padding:0 34px}
  .panel--about{left:0}
  .panel--why{left:360px}
  .panel--benefits{left:720px}
  .fold{position:absolute;top:0;width:1px;height:760px;background:rgba(0,0,0,.12)}
  .brand{position:absolute;top:58px;left:34px;display:flex;align-items:center;gap:12px}
  .brand-dot{width:40px;height:40px;border-radius:50%;background:var(--brand-blue)}
  .brand-name{color:var(--brand-blue);font-weight:500;font-size:15px;line-height:1.25;letter-spacing:.06em;text-transform:uppercase}
  .panel-title{position:absolute;color:#fff;font-weight:800;text-transform:uppercase;letter-spacing:.01em;line-height:1.1}
  .panel--about .panel-title{top:168px;left:40px;font-size:28px}
  .panel--why .panel-title{top:150px;left:34px;font-size:24px}
  .panel-title .subtitle{display:block;font-weight:400;font-size:22px}
  .panel--benefits .panel-title{top:150px;left:34px;font-size:22px}
  .panel-body{position:absolute;left:34px;right:34px;color:var(--text);font-size:10.5px;line-height:1.55;text-align:justify}
  .panel--about .panel-body{top:330px}
  .panel--why .panel-body{top:262px}
  .panel--benefits .panel-body{top:262px;text-align:center}
  .panel-body p{margin-bottom:12px}
  .principal{color:var(--ink);font-weight:800;font-size:19px;line-height:1.2;text-transform:uppercase;margin-bottom:22px;text-align:left}
  .credentials{position:absolute;left:34px;bottom:56px;display:flex;align-items:center;gap:12px}
  .credentials .brand-dot{width:30px;height:30px}
  .credentials .mini-name{color:var(--brand-blue);font-weight:500;font-size:11px;letter-spacing:.06em;text-transform:uppercase}
  .badge{width:90px;height:40px;border:3px solid var(--badge);background:rgba(142,154,134,.15)}
</style>
</head>
<body>
  <main class="brochure">
    <svg class="brochure-bg" width="1080" height="760" viewBox="0 0 1080 760" aria-hidden="true">
      <rect width="1080" height="760" fill="var(--paper)"/>
      <polygon points="0,0 360,0 360,210 0,230" fill="var(--ink)"/>
      <polygon points="360,0 720,0 720,220 360,240" fill="var(--ink-soft)"/>
      <polygon points="720,0 1080,0 1080,210 720,230" fill="var(--ink)"/>
      <polygon points="360,0 1080,0 1080,0 360,150" fill="var(--crimson)"/>
      <polygon points="0,170 28,222 0,240" fill="var(--crimson)"/>
    </svg>
    <div class="fold" style="left:360px"></div>
    <div class="fold" style="left:720px"></div>

    <section class="panel panel--about">
      <div class="brand">
        <span class="brand-dot"></span>
        <span class="brand-name">Northgate Accounting<br>&amp; Consulting, LLC</span>
      </div>
      <h2 class="panel-title">About</h2>
      <div class="panel-body">
        <h3 class="principal">About Marian T Holloway, MSA EA (Principal)</h3>
        <p>I have a Masters' Degree in accounting and am an QDX Enrolled Agent. I am also a LedgerBook Advanced Certified Consultant in both the online and desktop products including Enterprise and Point of Sale. I provide individual and small business tax services. Accounting, bookkeeping, QDX representation, insurance audit representation, business license assistance and more. I have experience working with a wide variety of clients from the point where they first decide they want to start a business. They are often unsure about what to do first. I have a lot of experience to offer you. What a joy it is to watch success in action!</p>
      </div>
      <div class="credentials">
        <span class="brand-dot"></span>
        <span class="mini-name">Northgate</span>
        <span class="badge" role="img" aria-label="Enrolled agent credential badge"></span>
      </div>
    </section>

    <section class="panel panel--why">
      <h2 class="panel-title">Tax<br>Preparation<span class="subtitle">Why hire us?</span></h2>
      <div class="panel-body">
        <p>I have a Masters' Degree in accounting and am an QDX Enrolled Agent. I am also a LedgerBook Advanced Certified Consultant in both the online and desktop products including Enterprise and Point of Sale. I provide individual and small business tax services. Accounting, bookkeeping, QDX representation, insurance audit representation, business license assistance and more.</p>
        <p>I have experience working with a wide variety of clients. Preparing your own income tax return can be a task that leaves you with more questions than answers. According to a study released by the National Accounting Review Office last year, most taxpayers (77% of 71 million taxpayers) believe they benefited from using a professional tax preparer.</p>
        <p>Whether we like it or not, today's tax laws are so complicated that filing a relatively simple return can be confusing. It is just too easy to overlook deductions and credits to which you are entitled. Even if you use a computer software program there's no substitute for the assistance of an experienced tax professional. Want to start a business? They are often unsure about what to do first. I have a lot of experience to offer you. What a joy it is to watch success in action!</p>
      </div>
    </section>

    <section class="panel panel--benefits">
      <h2 class="panel-title">Here's<br>what your get...</h2>
      <div class="panel-body">
        <p>Your tax return will be checked and rechecked by our computer software identifying potential problems the QDX may look at more closely and reviewing the math to limit QDX contacts.</p>
        <p>Your tax return can be filed electronically so you will get a refund back quicker.</p>
        <p>Our staff will show you how to adjust your payroll withholding to get more money back each week. Why give the QDX an interest free loan for up to 16 months.</p>
        <p>We will show you potential deductions to limit your tax liability for next year. In addition, we will give you a sheet of commonly overlooked deductions to limit the following year's tax liability.</p>
        <p>Books a Mess: No Problem! If you own a small business and haven't kept up your bookkeeping, don't worry. We can help you. We'll prepare your bookkeeping for the year, prepare a full Schedule C as well as your personal income tax return. Then we'll help you set up an easy system that allows you to keep your books in tip-top shape next year.</p>
      </div>
    </section>
  </main>
</body>
</html>
```